Etiketten für Honiggläser gesucht
sehr kreativer Entwurf, in dem alle umfangreichen Vorgaben berücksichtigt wurden. q4472 ist sehr service- und lösungsorientiert. Arbeitet sehr schnell und exzellent.
Zielgruppe
Wir sind eine junge Hobbyimkerei und produzieren unsere eigenen Honigsorten. Zielgruppe ist jeder, der Honig mag.
Aufgabenstellung
Das zu entwerfende Etiketten_Design soll grundsätzlich ein „absoluter Hingucker“ werden, einen hohen Wiedererkennungswert besitzen, edel erscheinen und die Hochwertigkeit des Produktes zum Ausdruck bringen.
Im engeren Sinn sollen zwei voneinander unabhängige Etikettenteile entworfen werden, die aber im Design eine Einheit bilden sollen:
Beim ersten Teil handelt es sich um den sogenannten Gewährverschluss; er verbindet den Deckel mit dem Glas und zerreißt beim ersten Öffnen des Deckels. Der Gewährverschluss soll etwa 2 cm breit und 8 cm lang sein, und unter anderem von unserem Firmenlogo (siehe Datei) geziert werden. Bei dem Logo darf die Grafik und der Hintergrund in der Farbe variieren, und der Schriftzug kann entfallen, andere Änderungen dürfen jedoch nicht vorgenommen werden. Das Logo kann bei Bedarf gerne in anderen Dateiformaten zur Verfügung gestellt werden.
Den zweiten Teil stellt das eigentliche Produktetikett dar. Für dieses gibt es keine Größen- und Formvorgaben, allerdings müssen folgende Inhalte Berücksichtigung finden: Die Daten des Imkers (bitte folgende Platzhalter verwenden „Firmenname“, „Vorname1 & Vorname2 Nachname“, „Straße + Hausnummer“, „PLZ + Ortsname“, „Internetseite“ und „Emailadresse“) sowie den Angaben „500g“, „Mindestens haltbar bis:“ (dahinter oder darunter bitte weißen Freiraum für den Stempelaufdruck des Datums lassen), „Trocken, dunkel und vor Wärme geschützt lagern!“, und – ganz wichtig – die „Honigsorte“ mit den vorangestellten Worten „feinster deutscher“ (, z.B. „feinster deutscher Rapshonig“).
Jede Honigsorte soll mit einer Farbe verknüpft werden, sodass der Kunde schnell erkennen kann um welche Honigsorte es sich im Glas handelt (beispielsweise gelb für Rapshonig, grün für Waldhonig, usw.). Dafür soll die jeweilige Honigsortenfarbe, in welcher Form auch immer, das Etikett oder einen bestimmten Bereich davon domini..

```html
<!DOCTYPE html>
<html lang="de">
<head>
<meta charset="utf-8">
<title>Honigetiketten – Imkerei Roderich</title>
<link rel="stylesheet" href="https://fonts.googleapis.com/css2?family=Playfair+Display:wght@400;700&family=Libre+Caslon+Text:wght@400&display=swap">
<style>
  :root {
    --bg: #f4f3f1;
    --paper: #ffffff;
    --edge: #e2dfda;
    --ink: #2d2a26;
    --ink-soft: #6b665f;
    --raps: #e3c21f;
    --akazie: #7fa56a;
    --blueten: #b0639f;
  }
  * { margin: 0; padding: 0; box-sizing: border-box; }
  html, body { width: 1200px; height: 780px; overflow: hidden; background: var(--bg); }
  .canvas { position: relative; width: 1200px; height: 780px; }

  .label { position: absolute; top: 140px; width: 240px; height: 500px; }
  .label__shape { position: absolute; inset: 0; }
  .label__shape path { fill: var(--paper); stroke: var(--edge); stroke-width: 1; }
  .label__content { position: absolute; inset: 0; text-align: center; color: var(--ink); }

  .address {
    position: absolute; top: 34px; left: 0; right: 0;
    font-family: "Libre Caslon Text", serif; font-size: 7px; line-height: 10px; color: var(--ink-soft);
  }
  .brand {
    position: absolute; top: 106px; left: 0; right: 0;
    display: flex; flex-direction: column; align-items: center; gap: 6px;
  }
  .brand__dot { width: 18px; height: 18px; border-radius: 50%; background: var(--variety); }
  .brand__name {
    font-family: "Playfair Display", serif; font-weight: 400; font-size: 8px;
    letter-spacing: 1.5px; line-height: 10px; color: var(--ink-soft); text-transform: uppercase;
  }
  .variety-pre {
    position: absolute; top: 262px; left: 0; right: 0;
    font-family: "Playfair Display", serif; font-size: 15px; letter-spacing: 1.5px;
    line-height: 18px; text-transform: uppercase;
  }
  .variety-name {
    position: absolute; top: 306px; left: 0; right: 0;
    font-family: "Playfair Display", serif; font-weight: 700; font-size: 30px;
    letter-spacing: 1px; line-height: 32px; text-transform: uppercase;
  }
  .weight {
    position: absolute; top: 388px; left: 0; right: 0;
    font-family: "Playfair Display", serif; font-size: 12px; letter-spacing: 1px;
  }

  .label--raps { left: 100px; --variety: var(--raps); }
  .label--akazie { left: 380px; --variety: var(--akazie); }
  .label--blueten { left: 660px; --variety: var(--blueten); }

  .seal { position: absolute; left: 970px; top: 140px; width: 110px; height: 440px; }
  .seal__shape { position: absolute; inset: 0; }
  .seal__shape path { fill: var(--paper); stroke: var(--edge); stroke-width: 1; }
  .seal__brand {
    position: absolute; top: 26px; left: 0; right: 0;
    display: flex; flex-direction: column; align-items: center; gap: 6px;
  }
  .seal__square { width: 22px; height: 22px; border: 1.5px solid var(--ink); }
  .seal__name {
    font-family: "Playfair Display", serif; font-size: 7px; letter-spacing: 1px;
    line-height: 9px; text-transform: uppercase; color: var(--ink); text-align: center;
  }
  .seal__address {
    position: absolute; top: 330px; left: 10px; right: 10px;
    font-family: "Libre Caslon Text", serif; font-size: 6.5px; line-height: 9px;
    color: var(--ink-soft); text-align: center;
  }
</style>
</head>
<body>
<main class="canvas">

  <section class="label label--raps">
    <svg class="label__shape" viewBox="0 0 240 500" width="240" height="500" aria-hidden="true">
      <path d="M70,28 Q70,0 98,0 H142 Q170,0 170,28 V180 C170,215 239,220 239,265 V470 Q239,499 210,499 H30 Q1,499 1,470 V265 C1,220 70,215 70,180 Z"/>
    </svg>
    <div class="label__content">
      <p class="address">Nachname<br>Straße 23<br>12345 Ortsname<br>Internetseite<br>Emailadresse</p>
      <div class="brand"><span class="brand__dot"></span><p class="brand__name">Imkerei<br>Roderich</p></div>
      <p class="variety-pre">Feinster<br>Deutscher</p>
      <p class="variety-name">Raps<br>Honig</p>
      <p class="weight">500 g</p>
    </div>
  </section>

  <section class="label label--akazie">
    <svg class="label__shape" viewBox="0 0 240 500" width="240" height="500" aria-hidden="true">
      <path d="M70,28 Q70,0 98,0 H142 Q170,0 170,28 V180 C170,215 239,220 239,265 V470 Q239,499 210,499 H30 Q1,499 1,470 V265 C1,220 70,215 70,180 Z"/>
    </svg>
    <div class="label__content">
      <p class="address">Nachname<br>Straße 23<br>12345 Ortsname<br>Internetseite<br>Emailadresse</p>
      <div class="brand"><span class="brand__dot"></span><p class="brand__name">Imkerei<br>Roderich</p></div>
      <p class="variety-pre">Feinster<br>Deutscher</p>
      <p class="variety-name">Akazien<br>Honig</p>
      <p class="weight">500 g</p>
    </div>
  </section>

  <section class="label label--blueten">
    <svg class="label__shape" viewBox="0 0 240 500" width="240" height="500" aria-hidden="true">
      <path d="M70,28 Q70,0 98,0 H142 Q170,0 170,28 V180 C170,215 239,220 239,265 V470 Q239,499 210,499 H30 Q1,499 1,470 V265 C1,220 70,215 70,180 Z"/>
    </svg>
    <div class="label__content">
      <p class="address">Nachname<br>Straße 23<br>12345 Ortsname<br>Internetseite<br>Emailadresse</p>
      <div class="brand"><span class="brand__dot"></span><p class="brand__name">Imkerei<br>Roderich</p></div>
      <p class="variety-pre">Feinster<br>Deutscher</p>
      <p class="variety-name">Blüten<br>Honig</p>
      <p class="weight">500 g</p>
    </div>
  </section>

  <section class="seal">
    <svg class="seal__shape" viewBox="0 0 110 440" width="110" height="440" aria-hidden="true">
      <path d="M55,1 A54,54 0 0 1 98,88 V430 Q98,439 89,439 H21 Q12,439 12,430 V88 A54,54 0 0 1 55,1 Z"/>
    </svg>
    <div class="seal__brand"><span class="seal__square"></span><p class="seal__name">Imkerei<br>Roderich</p></div>
    <p class="seal__address">Vorname1 &amp; Vorname2<br>Nachname<br>Straße 23<br>12345 Ortsname<br>Internetseite<br>Emailadresse</p>
  </section>

</main>
</body>
</html>
```